基本レイアウトについては
https://zumelo.com/diagrams/XR8k21pTbvNDWfeL
もしくは、添付データのワイヤーをご参照ください。
レイアウトについては必ずしも上記に準じている必要はありません。
ご自由にご提案いただいても結構です。

全体の雰囲気としては
http://www.tomirei-wedding.net/
http://www.hokumorisanjingu.or.jp/
のような、桜色をつかいながら
あまり古臭くなり過ぎないようにアピールできればと思います。

また、製品は
http://www.seiryu-kojin.co.jp/goods/luvasystem
http://www.gw-tmr.co.jp/
のものを使用しています。

美容室へ来られる方は、近隣の方が多く、
和髪以外での競争力はあまりないため、WEB上では
美容師への和髪の講習などの訴求時に、
信頼性を高めるような用途が多くなりそうです。

そのため、上記参考サイトのような
ちょっとしたスタイリッシュさを目指しています。
http://qrvmd.ozu.ne.jp/0597214483/index.html
ホワイト、桜色をベースに、落ち着いた印象に出来ればと存じます。
素材については、
下記URLよりダウンロードしたものをご利用いただければ幸甚です。
http://plumvault.jp/download/a4f19e02bd7753c6e1088f2d94ab37c51e0d2a96

こちらだけですと、制作が難しいと思いますので
http://mobre.jp/
などから、5000円程度までならこちらにて購入可能です。カンプデータにて作成頂き、
納品時に当方にて購入したデータに差し替えていただければと存じます。

【参考サイト】
↑色合い、印象が気に入っています

http://www.gw-tmr.co.jp/
↑使用している製品のホームページです

http://basement-parts.com/2012/166.html
http://basement-parts.com/2011/115.html
↑フッター部分の参照です

基本レイアウト
については、必ずしも忠実である必要はありません。

是非ご提案お待ちしております。
何卒よろしくお願いいたします。

クライアント様との協議の結果こちらの案を採用させていただきました。
上品さと柔らかさのバランスがとてもよく、
視認性も高く、要望を全て満たしておりましたので
こちらの案を採用いたしました。

この度は多数ご提案いただきありがとうございました。
当選に至らなかったランサー様におかれましては大変心苦しいのですが、
またの機会にぜひご提案いただければ幸甚です。
引き続き何卒よろしくお願いいたします。

```html
<!DOCTYPE html>
<html lang="ja">
<head>
<meta charset="utf-8">
<title>ミワコ美容室</title>
<link rel="stylesheet" href="https://fonts.googleapis.com/css2?family=Noto+Sans+JP:wght@400;700&family=Yuji+Syuku&display=swap">
<style>
:root{
  --sakura:#f4c9d2;
  --sakura-light:#fbe9ee;
  --sakura-deep:#d98396;
  --rose:#b9566c;
  --footer:#c9727f;
  --footer-dark:#a8505f;
  --ink:#4a3b3d;
  --muted:#8c7b7e;
  --line:#e8d3d8;
}
*{box-sizing:border-box;margin:0;padding:0}
html,body{width:720px;height:1200px;overflow:hidden;background:#fff}
body{font-family:"Noto Sans JP",sans-serif;color:var(--ink);font-size:9px;position:relative}
.brush{font-family:"Yuji Syuku",serif;font-weight:400}
.header{position:absolute;left:0;top:0;width:720px;height:342px;background:linear-gradient(90deg,#fff 0%,var(--sakura-light) 40%,var(--sakura) 100%)}
.header-photo{position:absolute;left:204px;top:0;width:228px;height:330px;background:linear-gradient(160deg,#e9d6cc,#2d2f55 75%)}
.blossoms{position:absolute;left:540px;top:0;width:180px;height:342px;background:radial-gradient(circle at 120px 50px,#f7b7c6 0 22px,transparent 23px),radial-gradient(circle at 150px 170px,#f7b7c6 0 16px,transparent 17px),radial-gradient(circle at 60px 230px,#f9c8d3 0 11px,transparent 12px)}
.tagline{position:absolute;left:440px;top:20px;height:200px;writing-mode:vertical-rl;font-size:10px;line-height:1.8;color:var(--ink)}
.logo{position:absolute;left:476px;top:18px;font-size:40px;color:var(--rose);writing-mode:vertical-rl;line-height:1;letter-spacing:2px}
.contact-head{position:absolute;left:462px;top:284px;color:var(--rose)}
.contact-head .tel{font-size:15px;font-weight:700;line-height:1.3}
.contact-head .tel small{font-size:8px}
.contact-head p{font-size:8px;color:var(--ink);line-height:1.5}
.nav{position:absolute;left:210px;top:350px;width:498px;height:22px;display:flex;border-bottom:3px solid var(--sakura)}
.nav a{flex:1;text-align:center;font-size:10px;color:var(--ink);text-decoration:none;line-height:20px}
.nav a.current{color:var(--sakura-deep)}
.sidebar{position:absolute;left:210px;top:384px;width:115px}
.call-box{border:1px solid var(--sakura-deep);height:108px;padding:8px 6px;text-align:center;background:#fff}
.call-box h3{font-size:10px;color:var(--ink);line-height:1.4}
.call-box .tel{font-size:15px;font-weight:700;color:var(--rose);margin:4px 0}
.call-box p{font-size:7.5px;text-align:left;line-height:1.6}
.side-menu{list-style:none;margin-top:8px;border-top:2px solid var(--sakura-deep)}
.side-menu li{border-bottom:1px solid var(--line);padding:4px 6px;font-size:9.5px;color:var(--rose)}
.side-menu li::before{content:"▸ ";color:var(--sakura-deep)}
.side-banner{margin-top:8px;height:50px;background:linear-gradient(90deg,var(--sakura-light),var(--sakura));padding:6px;font-size:11px;color:var(--rose)}
.about-banner{position:absolute;left:335px;top:384px;width:373px;height:108px;background:linear-gradient(90deg,var(--sakura-light),#fff)}
.about-banner h2{position:absolute;left:10px;top:10px;font-size:16px;color:var(--rose)}
.about-banner p{position:absolute;left:10px;top:42px;font-size:11.5px;line-height:1.7}
.about-photo{position:absolute;right:0;top:0;width:140px;height:108px;background:linear-gradient(90deg,#efe6e3,#3a3434)}
.news{position:absolute;left:335px;top:532px;width:373px}
.news h2{font-size:14px;border-bottom:1px solid var(--line);padding-bottom:4px;margin-bottom:4px}
.news ul{list-style:none}
.news li{font-size:8.5px;border-bottom:1px dotted var(--line);padding:5px 4px;color:var(--muted)}
.news li span{margin-right:12px}
.welcome{position:absolute;left:335px;top:720px;width:373px;height:168px;background:linear-gradient(90deg,#f4eaea,var(--sakura-light))}
.welcome-photo{position:absolute;left:0;top:0;width:110px;height:168px;background:linear-gradient(180deg,#3b2f2c,#d7c0b5)}
.welcome h2{position:absolute;left:160px;top:12px;font-size:20px;color:var(--rose);line-height:1.2}
.welcome h2 small{display:block;font-size:10px;color:var(--ink);padding-left:30px}
.products{position:absolute;left:118px;top:80px;width:120px;height:82px;background:linear-gradient(180deg,#f3f3f3,#d8dadc)}
.shop{position:absolute;right:6px;top:70px;width:125px;height:92px;background:linear-gradient(180deg,#6f8f6a,#dfe5dc)}
.intro{position:absolute;left:210px;top:900px;width:498px;font-size:8.5px;line-height:1.9}
.footer{position:absolute;left:0;top:996px;width:720px;height:180px;background:var(--footer);color:#fff}
.footer .logo-foot{position:absolute;left:210px;top:20px;font-size:24px}
.footer .tel{position:absolute;left:210px;top:60px;font-size:15px;font-weight:700}
.footer .tel small{font-size:8px}
.footer .addr{position:absolute;left:210px;top:84px;font-size:7.5px;line-height:1.6}
.footer ul{position:absolute;list-style:none;font-size:8px;line-height:1.8}
.foot-menu{left:372px;top:42px}
.foot-sub{left:552px;top:42px}
.copy{position:absolute;left:0;top:1176px;width:720px;height:24px;background:var(--footer-dark);color:#fff;font-size:7px;text-align:center;line-height:24px}
</style>
</head>
<body>
<header class="header">
  <div class="header-photo" role="img" aria-label="和装で日本髪を結った女性の写真"></div>
  <div class="blossoms" role="img" aria-label="桜の花びらの装飾"></div>
  <p class="tagline">地域の皆様にやさしく<br>和髪の文化を伝える美容室です</p>
  <h1 class="logo brush">ミワコ美容室</h1>
  <div class="contact-head">
    <div class="tel">tel 045-712-3904 <small>(要予約)</small></div>
    <p>営業時間 9:00〜19:00 / 定休日 毎週火曜日<br>神奈川県みどり市桜町1-2-3</p>
  </div>
</header>
<nav class="nav">
  <a class="current">HOME</a><a>メニュー・料金</a><a>製品へのこだわり</a><a>よくある質問</a><a>店舗案内</a>
</nav>
<aside class="sidebar">
  <div class="call-box">
    <h3>お電話でお気軽に<br>ご連絡ください</h3>
    <div class="tel">045-712-3904</div>
    <p>■ 平日 9:00〜18:00<br>■ 土曜・日 1月休業日<br>■ 臨時休業あり</p>
  </div>
  <ul class="side-menu">
    <li>HOME</li><li>メニュー・料金</li><li>製品へのこだわり</li><li>和髪について</li><li>よくある質問</li><li>店舗案内</li>
  </ul>
  <div class="side-banner brush">和髪について</div>
</aside>
<section class="about-banner">
  <h2 class="brush">和髪について</h2>
  <p class="brush">お客さまは、和髪を求めております。<br>日本の美に触れてみませんか？</p>
  <div class="about-photo" role="img" aria-label="結い上げた日本髪の後ろ姿の写真"></div>
</section>
<section class="news">
  <h2 class="brush">新着情報</h2>
  <ul>
    <li><span>2014.00.00</span>ニュース入りますニュース入りますニュース入ります</li>
    <li><span>2014.00.00</span>ニュース入りますニュース入りますニュース入ります</li>
    <li><span>2014.00.00</span>ニュース入りますニュース入りますニュース入ります</li>
    <li><span>2014.00.00</span>ニュース入りますニュース入りますニュース入ります</li>
    <li><span>2014.00.00</span>ニュース入りますニュース入りますニュース入ります</li>
  </ul>
</section>
<section class="welcome">
  <div class="welcome-photo" role="img" aria-label="髪を結う施術中の写真"></div>
  <h2 class="brush"><small>ようこそ</small>ミワコ美容室へ</h2>
  <div class="products" role="img" aria-label="使用しているヘアケア製品の写真"></div>
  <div class="shop" role="img" aria-label="店舗外観の写真"></div>
</section>
<p class="intro">ミワコ美容室は、地域の皆様に愛される美容室として和髪の技術を大切にしております。<br>
頭皮にやさしい製品を使用し、一人ひとりに合わせた施術をご提案いたします。<br>
美容師の方への和髪講習も行っておりますので、お気軽にお問い合わせください。<br>
皆様のご来店を心よりお待ちしております。</p>
<footer class="footer">
  <div class="logo-foot brush">ミワコ美容室</div>
  <div class="tel">tel 045-712-3904 <small>(要予約)</small></div>
  <p class="addr">営業時間 9:00〜19:00 / 定休日 毎週火曜日<br>神奈川県みどり市桜町1-2-3</p>
  <ul class="foot-menu"><li>HOME</li><li>メニュー・料金</li><li>製品へのこだわり</li><li>和髪について</li><li>よくある質問</li><li>店舗案内</li></ul>
  <ul class="foot-sub"><li>プライバシーポリシー</li><li>サイトマップ</li></ul>
</footer>
<div class="copy">Copyright©2014 ミワコ美容室 All Rights Reserved.</div>
</body>
</html>
```